Sign listing benefits of Wash and Fold Service

Sign 48 inches wide and 24 inches height to showcase service listed above.
Benefits include:
Saves Money
Saves Time
Convenient
Stain Treatment

Looking for something colorful (Blue and white are our business colors) the look of a laundromat business.

```html
<!DOCTYPE html>
<html lang="en">
<head>
<meta charset="UTF-8">
<title>Wash and Fold Service – Benefits Sign</title>
<link rel="stylesheet" href="https://fonts.googleapis.com/css2?family=Barlow+Condensed:wght@500;600&display=swap">
<style>
  :root {
    --brand-blue: #283891;
    --accent-sky: #4fc3f0;
    --accent-sky-soft: #bfe6f7;
    --panel-light: #e8e9ea;
    --text-light: #eef0f6;
    --backdrop: #d9dadc;
  }
  * { margin: 0; padding: 0; box-sizing: border-box; }
  html, body {
    width: 1200px;
    height: 675px;
    overflow: hidden;
    background: var(--backdrop);
  }
  .sign {
    position: absolute;
    left: 40px;
    top: 57px;
    width: 1120px;
    height: 560px;
    display: grid;
    grid-template-columns: repeat(4, 1fr);
    font-family: "Barlow Condensed", "Arial Narrow", sans-serif;
  }
  .benefit {
    position: relative;
    overflow: hidden;
  }
  .benefit--dark { background: var(--brand-blue); color: var(--text-light); }
  .benefit--light { background: var(--panel-light); color: var(--brand-blue); }
  .benefit__frame {
    position: absolute;
    inset: 0;
    width: 100%;
    height: 100%;
  }
  .benefit__icon {
    position: absolute;
    left: 90px;
    width: 100px;
    height: 100px;
    border-radius: 50%;
  }
  .benefit__icon--top { top: 118px; }
  .benefit__icon--bottom { top: 350px; }
  .benefit--dark .benefit__icon {
    background: radial-gradient(circle at 50% 40%, var(--accent-sky-soft), #d3dcef 75%);
  }
  .benefit--light .benefit__icon {
    background: radial-gradient(circle at 50% 40%, #3f6ec0, #2f4aa0 75%);
  }
  .benefit__tick {
    position: absolute;
    left: 90px;
    top: 350px;
    width: 100px;
    height: 100px;
  }
  .benefit__label {
    position: absolute;
    left: 0;
    right: 0;
    text-align: center;
    font-weight: 500;
    font-size: 50px;
    line-height: 55px;
    letter-spacing: 0.2px;
  }
  .benefit__label--bottom { top: 340px; }
  .benefit__label--top { top: 112px; }
  .benefit__label--single { top: 152px; }
  .ring { fill: none; stroke: var(--accent-sky); stroke-width: 2; stroke-dasharray: 6 5; }
  .connector { stroke: var(--accent-sky); stroke-width: 2; stroke-dasharray: 6 5; }
  .tick-line { fill: none; stroke-width: 4; stroke-linecap: round; stroke-linejoin: round; }
</style>
</head>
<body>
<main class="sign" aria-label="Wash and fold service benefits">

  <section class="benefit benefit--dark">
    <svg class="benefit__frame" viewBox="0 0 280 560" aria-hidden="true">
      <circle class="ring" cx="140" cy="168" r="96"/>
      <circle cx="140" cy="168" r="86" fill="var(--panel-light)"/>
      <line class="connector" x1="140" y1="264" x2="140" y2="340"/>
    </svg>
    <div class="benefit__icon benefit__icon--top" role="img" aria-label="Line icon of a coin held above an open hand"></div>
    <h2 class="benefit__label benefit__label--bottom">Saves<br>Money</h2>
  </section>

  <section class="benefit benefit--light">
    <svg class="benefit__frame" viewBox="0 0 280 560" aria-hidden="true">
      <line class="connector" x1="140" y1="228" x2="140" y2="304"/>
      <circle class="ring" cx="140" cy="400" r="96"/>
      <circle cx="140" cy="400" r="86" fill="var(--brand-blue)"/>
    </svg>
    <div class="benefit__icon benefit__icon--bottom" role="img" aria-label="Line icon of a clock above an open hand"></div>
    <h2 class="benefit__label benefit__label--top">Saves<br>Time</h2>
  </section>

  <section class="benefit benefit--dark">
    <svg class="benefit__frame" viewBox="0 0 280 560" aria-hidden="true">
      <circle class="ring" cx="140" cy="168" r="96"/>
      <circle cx="140" cy="168" r="86" fill="var(--panel-light)"/>
      <line class="connector" x1="140" y1="264" x2="140" y2="340"/>
    </svg>
    <div class="benefit__icon benefit__icon--top" role="img" aria-label="Line icon of a clean shirt on a hanger"></div>
    <h2 class="benefit__label benefit__label--bottom">Stain<br>Treatment</h2>
  </section>

  <section class="benefit benefit--light">
    <svg class="benefit__frame" viewBox="0 0 280 560" aria-hidden="true">
      <line class="connector" x1="140" y1="228" x2="140" y2="304"/>
      <circle class="ring" cx="140" cy="400" r="96"/>
      <circle cx="140" cy="400" r="86" fill="var(--brand-blue)"/>
    </svg>
    <svg class="benefit__tick" viewBox="0 0 100 100" aria-hidden="true">
      <path class="tick-line" d="M28 52l16 16l30 -34" stroke="var(--accent-sky)"/>
    </svg>
    <h2 class="benefit__label benefit__label--single">Convenient</h2>
  </section>

</main>
</body>
</html>
```